Fish guide business card

Buisiness card

Target Market(s)

Visitors to Campbell River Bc wanting to catch fish in the ocean and have a memorable adventure fun filled day

Industry/Entity Type

Tourism

Contact Information for Business Card

Phone number 250 318 two cards Ray 250 318 7262 other card Lou 250 6093714 both have email info@lwgullrocktours.com and website www.lwgullrocktours.com

Requirements
Must have
• Email, website , name , phone , logo , Campbell River BC
Nice to have
• Uploaded pictures have boat and man with fish picture

```html
<!DOCTYPE html>
<html lang="en">
<head>
<meta charset="utf-8">
<title>Gull Rock Tours – Business Card</title>
<link href="https://fonts.googleapis.com/css2?family=Montserrat:wght@300;400;500;700;800&display=swap" rel="stylesheet">
<style>
  :root {
    --navy: #292462;
    --sky: #03a4e3;
    --sky-soft: #22aae2;
    --white: #ffffff;
    --backdrop: #d6d6d6;
    --photo-sea: #3c4f6e;
    --photo-sky: #c9ced6;
  }
  * { margin: 0; padding: 0; box-sizing: border-box; }
  html, body {
    width: 1200px; height: 1200px; overflow: hidden;
    background: var(--backdrop);
    font-family: "Montserrat", sans-serif;
  }
  .card { position: absolute; overflow: hidden; }
  .card svg { display: block; }
  .card-front { left: 267px; top: 119px; width: 697px; height: 397px; background: var(--white); }
  .card-back { left: 267px; top: 654px; width: 711px; height: 405px; background: var(--navy); }

  .brand-name {
    position: absolute; left: 483px; top: 56px;
    color: var(--navy); font-weight: 700; line-height: 1;
  }
  .brand-name .line-main { display: block; font-size: 27px; }
  .brand-name .line-sub { display: block; font-size: 18px; letter-spacing: 5px; margin-top: 6px; }

  .person { position: absolute; left: 51px; top: 328px; line-height: 1; }
  .person-name { font-size: 32px; font-weight: 800; color: var(--white); letter-spacing: -0.5px; }
  .person-name .surname { color: var(--navy); }
  .person-role { font-size: 19px; font-weight: 300; color: var(--white); margin-top: 8px; }

  .contact-list { position: absolute; left: 374px; top: 218px; list-style: none; color: var(--white); font-size: 15px; font-weight: 500; }
  .contact-item { display: flex; align-items: center; height: 26px; margin-bottom: 9px; }
  .contact-item svg { width: 18px; height: 18px; margin-right: 12px; }
  .contact-divider { width: 294px; height: 4px; margin: 10px 0 14px;
    background-image: radial-gradient(circle, var(--sky) 1.6px, transparent 1.8px);
    background-size: 10px 4px; }
  .contact-item.web { color: var(--sky); }

  .back-badge {
    position: absolute; left: 227px; top: 62px; width: 240px; height: 240px;
    border-radius: 50%; background: var(--white);
    display: flex; flex-direction: column; align-items: center; justify-content: center;
    color: var(--navy); font-weight: 700; line-height: 1;
  }
  .back-badge .line-main { font-size: 30px; }
  .back-badge .line-sub { font-size: 22px; letter-spacing: 6px; margin-top: 8px; }

  .back-divider { position: absolute; left: 0; top: 341px; width: 100%; height: 9px; background: var(--white); }
  .back-footer {
    position: absolute; left: 0; top: 350px; width: 100%; height: 55px; background: var(--sky-soft);
    display: flex; align-items: center; justify-content: center; color: var(--white); font-size: 15px; font-weight: 500;
  }
  .back-footer svg { width: 20px; height: 20px; margin-right: 12px; }
</style>
</head>
<body>

<section class="card card-front">
  <svg width="697" height="397" viewBox="0 0 697 397">
    <defs>
      <linearGradient id="photoTones" x1="0" y1="0" x2="0" y2="1">
        <stop offset="0" stop-color="#c9ced6"/>
        <stop offset="0.15" stop-color="#56698a"/>
        <stop offset="0.6" stop-color="#3c4f6e"/>
        <stop offset="1" stop-color="#8a8f92"/>
      </linearGradient>
    </defs>
    <polygon points="0,0 359,0 317,198 359,397 0,397" fill="url(#photoTones)" role="img" aria-label="Photo of the founder on a boat holding a large salmon"/>
    <path d="M317 198 L356 158 Q363 151 374 151 L697 151 L697 198 Z" fill="var(--sky)"/>
    <polygon points="317,198 697,198 697,397 359,397" fill="var(--navy)"/>
    <path d="M0 314 L322 314 Q334 314 334 328 L334 340 L282 397 L0 397 Z" fill="var(--sky)"/>
    <circle cx="423" cy="82" r="44" fill="none" stroke="var(--navy)" stroke-width="3"/>
  </svg>

  <div class="brand-name">
    <span class="line-main">Gull Rock</span>
    <span class="line-sub">Tours</span>
  </div>

  <div class="person">
    <div class="person-name">RAY <span class="surname">MARLOW</span></div>
    <div class="person-role">FOUNDER</div>
  </div>

  <ul class="contact-list">
    <li class="contact-item">
      <svg viewBox="0 0 24 24"><path d="M6.6 2.5 9 6.8 7.3 8.9c.9 2.6 2.8 5.2 5.3 6.6l2-1.7 4.3 2.4-1.4 3.8c-7.5-.4-13.3-6.4-13.5-13.9z" fill="#fff"/></svg>
      250 318 7262
    </li>
    <li class="contact-item">
      <svg viewBox="0 0 24 24"><rect x="2" y="5" width="20" height="14" fill="#fff"/><path d="M2 5l10 8 10-8M2 19l7-7M22 19l-7-7" stroke="var(--navy)" stroke-width="1.5" fill="none"/></svg>
      info@lwgullrocktours.com
    </li>
    <li class="contact-divider"></li>
    <li class="contact-item web">
      <svg viewBox="0 0 24 24" fill="none" stroke="var(--sky)" stroke-width="1.6"><circle cx="12" cy="12" r="10"/><ellipse cx="12" cy="12" rx="4.5" ry="10"/><path d="M2 12h20M4 6.5h16M4 17.5h16M12 2v20"/></svg>
      www.lwgullrocktours.com
    </li>
  </ul>
</section>

<section class="card card-back">
  <div class="back-badge">
    <span class="line-main">Gull Rock</span>
    <span class="line-sub">Tours</span>
  </div>
  <div class="back-divider"></div>
  <div class="back-footer">
    <svg viewBox="0 0 24 24" fill="none" stroke="#fff" stroke-width="1.6"><circle cx="12" cy="12" r="10"/><ellipse cx="12" cy="12" rx="4.5" ry="10"/><path d="M2 12h20M4 6.5h16M4 17.5h16M12 2v20"/></svg>
    www.lwgullrocktours.com
  </div>
</section>

</body>
</html>
```